Kelvo.cn needs pages to be re-designed

www.kelvo.cn is our current new site which was launched in April.
We're a financial services website in the crowdfunding space in China to connect borrower's and lender's.

test.kelvo.cn is our test site
u: test
p: fogpine
http://test.kelvo.cn/
http://test.kelvo.cn/user/accounts/new_lender
http://test.kelvo.cn/user/accounts/new_borrower
http://test.kelvo.cn/introductions/protection
http://test.kelvo.cn/introductions
http://test.kelvo.cn/introductions/kelvo_admin
http://test.kelvo.cn/introductions/contact
Some of the pages have pop-ups in the bloc's of the pages. Please click the links, to see more content.

User's currently criticize the website for being:
- Too Western looking
- Too simple, too little content
- Content NOT in the pop-ups are too simple
- Pictures are too big and too much blank space
- Relevant information is not there when needed
- The pictures are too generic

What we would like to do is re-design those pages with the same color scheme and style to be more compelling, efficient, non-intimidating and easy-to-use. Our audience is Ages 25-35 predominantly male investors.
We are looking for more ideas to make the content match the style, while bridging western and chinese design. Our ultimate goal is to increase registrants to the website and highlight our core competitive advantages.

Some competitors websites are:
www.tobumix.com
www.fesca.com
www.zwqvolt.com

Reason: Not enough good designs that follow the prompt. Same style, better information layout!

Reason: Still have not received a design we're satisfied with

Reason: WE DONT WANT A COMPLETE REDESIGN OF PAGES . KEEP THE EXACT SAME COLOR AND STYLE - WE WANT CONTENT RE-DESIGN! THE BLOCS ARE TOO SIMPLE - WE WANT MORE CONTENT INSIDE.

Reason: no new designs

Reason: no new designs

Reason: other non-registered pages need to be re-designed

```html
<!DOCTYPE html>
<html lang="en">
<head>
<meta charset="utf-8">
<title>Kelvo.cn – Safe, efficient and transparent investment</title>
<link href="https://fonts.googleapis.com/css2?family=Open+Sans:wght@300;400;600;700&display=swap" rel="stylesheet">
<style>
:root{
  --green:#5aa52c;
  --green-dark:#4a8f22;
  --orange:#f3a21d;
  --blue:#2f9fd8;
  --red:#ef5a5c;
  --ink:#333;
  --muted:#888;
  --line:#e3e3e3;
  --band:#eeeeee;
  --white:#fff;
}
*{box-sizing:border-box;margin:0;padding:0}
html,body{width:1200px;height:2324px;overflow:hidden}
body{font-family:"Open Sans",Arial,sans-serif;color:var(--ink);background:var(--white);position:relative;font-size:14px}
.wrap{width:900px;margin:0 auto;position:relative}

/* hero */
.hero{position:absolute;top:0;left:0;width:1200px;height:580px;
  background:linear-gradient(180deg,#dfe7ec 0%,#f3e6cf 40%,#f2c98e 62%,#d9a36b 78%,#c8b9a6 100%)}
.header{position:absolute;top:0;left:0;width:1200px;height:120px;background:rgba(255,255,255,.78)}
.brand{position:absolute;left:150px;top:22px;display:flex;align-items:center;gap:14px}
.brand-dot{width:56px;height:56px;border-radius:50%;background:var(--green)}
.brand-name{font-size:34px;font-weight:700;color:var(--green);line-height:1}
.brand-url{font-size:13px;color:var(--muted);margin-top:4px}
.top-meta{position:absolute;right:150px;top:22px;display:flex;gap:22px;font-size:14px;color:var(--ink);align-items:center}
.top-meta .phone{color:var(--green);font-weight:600}
.lang{width:24px;height:16px;background:#c6ccd6;border:1px solid #aab}
.nav{position:absolute;right:150px;top:80px;display:flex}
.nav a{display:block;padding:10px 22px;font-size:14px;color:var(--ink);text-decoration:none;border-left:1px solid var(--line)}
.nav a.active{background:var(--green);color:var(--white)}
.hero-title{position:absolute;left:390px;top:250px;color:var(--white);font-weight:300;line-height:1.15;text-shadow:0 1px 3px rgba(0,0,0,.15)}
.hero-title .l1{font-size:46px}
.hero-title .l2{font-size:46px}
.hero-title .l3{font-size:46px;font-weight:600}

/* features */
.features{position:absolute;top:590px;left:150px;width:900px;display:flex;gap:40px}
.card{width:195px;height:380px;background:var(--white);box-shadow:0 2px 6px rgba(0,0,0,.12)}
.card-top{height:170px;display:flex;align-items:center;justify-content:center}
.card-top svg{width:84px;height:84px}
.card.g .card-top{background:var(--green)} .card.o .card-top{background:var(--orange)}
.card.b .card-top{background:var(--blue)} .card.r .card-top{background:var(--red)}
.card-body{padding:18px 16px}
.card-body h3{font-size:16px;font-weight:700;margin-bottom:6px}
.card-body p{font-size:12px;color:var(--muted);line-height:1.55}
.card-link{display:inline-block;margin-top:14px;font-size:12px;color:var(--green);font-weight:600}
.successes{position:absolute;top:985px;left:150px;width:900px;display:flex;gap:40px;font-size:11px;color:var(--muted)}
.successes span{width:195px} .successes b{color:var(--orange);font-weight:600}

/* stats band */
.stats{position:absolute;top:1040px;left:0;width:1200px;height:130px;background:var(--green);color:var(--white)}
.stats .wrap{display:flex;align-items:center;height:130px}
.stat{width:200px}
.stat .v{font-size:34px;font-weight:600;font-style:italic;line-height:1.1}
.stat .k{font-size:12px;opacity:.9}
.stat.wide{width:260px}
.cta{margin-left:auto;display:flex;align-items:center;gap:10px}
.cta .ico{width:40px;height:40px}
.cta a{background:var(--orange);color:var(--white);font-weight:700;font-size:15px;padding:12px 22px;border-radius:3px;text-decoration:none}

/* loan table */
.loans{position:absolute;top:1195px;left:150px;width:900px;border-collapse:collapse;font-size:12px}
.loans th{background:var(--green);color:var(--white);font-weight:600;height:36px;text-align:left;padding:0 12px}
.loans td{height:38px;border-bottom:1px solid var(--line);padding:0 12px;color:#555}
.loans tr:nth-child(even) td{background:#fafafa}
.rate{display:inline-flex;width:20px;height:20px;border-radius:50%;border:1px solid #999;align-items:center;justify-content:center;font-size:10px;font-weight:700}
.rate.on{background:var(--green);border-color:var(--green);color:var(--white)}
.go{color:var(--green);font-weight:700}
.full{color:var(--ink);font-weight:700}

/* products */
.section-title{position:absolute;left:150px;font-size:15px;font-weight:700;color:var(--green)}
.products{position:absolute;top:1525px;left:150px;width:900px;display:flex;gap:20px}
.product{width:210px;height:230px;color:var(--white);text-align:center;padding-top:34px}
.product.photo{background:linear-gradient(160deg,#3c7d1e,#6fb33d);display:flex;align-items:center;justify-content:center;padding:0;font-size:56px;font-weight:700;letter-spacing:2px}
.product.o{background:var(--orange)} .product.b{background:var(--blue)} .product.r{background:var(--red)}
.product .t{font-size:12px;opacity:.95}
.product .pct{font-size:56px;font-weight:300;font-style:italic;line-height:1.2;margin:8px 0}
.product .s{font-size:11px;opacity:.9;padding:0 20px;line-height:1.5}

/* testimonials + newsletter */
.social{position:absolute;top:1790px;left:0;width:1200px;height:160px;background:var(--band)}
.social .wrap{display:flex;gap:30px;padding-top:20px}
.panel{background:var(--white);height:120px;width:435px;padding:14px 18px}
.panel h4{font-size:15px;font-weight:600;color:var(--green);text-align:center;margin-bottom:8px}
.testi{display:flex;gap:14px}
.avatar{width:52px;height:52px;border-radius:50%;background:linear-gradient(#d9cbb8,#a88f74);flex:none}
.testi p{font-size:11px;color:var(--muted);line-height:1.5}
.testi .who{color:var(--green);font-weight:600}
.panel .note{font-size:11px;color:var(--muted);text-align:center;margin-bottom:10px}
.signup{display:flex}
.signup span{flex:1;border:1px solid var(--line);height:32px;font-size:11px;color:#aaa;padding:8px 10px}
.signup b{background:var(--green);color:var(--white);font-size:12px;padding:8px 18px}

/* partners */
.partners{position:absolute;top:2005px;left:150px;width:900px;display:flex;justify-content:space-between;align-items:center}
.partner{display:flex;align-items:center;gap:10px;font-size:20px;font-weight:700;color:#2a5c9a}
.partner i{width:22px;height:22px;background:#c9302c;display:block}
.partner.t i{background:#2a5c9a}

/* footer */
.footer{position:absolute;top:2090px;left:0;width:1200px;height:234px;background:#f6f6f6;border-top:1px solid var(--line)}
.footer .wrap{display:flex;padding-top:22px}
.fcol h5{font-size:13px;color:var(--green);margin-bottom:10px}
.fcol ul{list-style:none;font-size:11px;color:#666;line-height:2}
.links{width:300px;display:flex;gap:40px}
.service{width:300px}
.icons{display:flex;gap:8px;margin:6px 0 10px}
.icons i{width:22px;height:22px;border-radius:50%;background:#555;display:block}
.address{width:300px}
.copy{position:absolute;bottom:14px;left:0;width:1200px;text-align:center;font-size:11px;color:#999}
</style>
</head>
<body>

<div class="hero" role="img" aria-label="Photo of a happy couple with raised arms on a sunny beach"></div>

<header class="header">
  <div class="brand">
    <span class="brand-dot"></span>
    <div><div class="brand-name">Kelvo</div><div class="brand-url">www.kelvo.cn</div></div>
  </div>
  <div class="top-meta"><span class="phone">400-555-0188</span><span>Log in</span><span class="lang"></span></div>
  <nav class="nav"><a class="active">Home</a><a>Security</a><a>Investment</a><a>Credit</a></nav>
</header>

<h1 class="hero-title">
  <div class="l1">Kelvo loan is a safe,</div>
  <div class="l2">Efficient and transparent</div>
  <div class="l3">investment platform.</div>
</h1>

<section class="features">
  <div class="card g">
    <div class="card-top"><svg viewBox="0 0 80 80" fill="none" stroke="#fff" stroke-width="4"><path d="M8 70h64M16 62V46M30 62V36M44 62V28M58 62V18"/><path d="M12 38 40 14l8 8 20-16" /><text x="52" y="46" fill="#fff" stroke="none" font-size="20" font-weight="700">$</text></svg></div>
    <div class="card-body"><h3>High Returns</h3><p>Annual rate of return up to 15%, far above bank deposits and other products.</p><span class="card-link">Learn more ›</span></div>
  </div>
  <div class="card o">
    <div class="card-top"><svg viewBox="0 0 80 80" fill="none" stroke="#fff" stroke-width="4"><path d="M40 6 68 16v22c0 18-12 30-28 36C24 68 12 56 12 38V16z"/><path d="m26 40 10 10 18-20"/></svg></div>
    <div class="card-body"><h3>100% Security</h3><p>Principal protection fund and strict risk control keep every lender safe.</p><span class="card-link">Learn more ›</span></div>
  </div>
  <div class="card b">
    <div class="card-top"><svg viewBox="0 0 80 80" fill="none" stroke="#fff" stroke-width="4"><circle cx="40" cy="40" r="32"/><circle cx="40" cy="40" r="22"/><text x="31" y="50" fill="#fff" stroke="none" font-size="28" font-weight="700">$</text></svg></div>
    <div class="card-body"><h3>Efficient</h3><p>Register in minutes, invest online and receive interest every single month.</p><span class="card-link">Learn more ›</span></div>
  </div>
  <div class="card r">
    <div class="card-top"><svg viewBox="0 0 80 80" fill="none" stroke="#fff" stroke-width="4"><path d="M14 34A28 28 0 0 1 66 28M66 46A28 28 0 0 1 14 52"/><path d="m60 18 6 10-10 4M20 62l-6-10 10-4"/><text x="31" y="50" fill="#fff" stroke="none" font-size="26" font-weight="700">£</text></svg></div>
    <div class="card-body"><h3>Transfer</h3><p>Need cash early? Transfer your loans to other lenders at any time.</p><span class="card-link">Learn more ›</span></div>
  </div>
</section>
<div class="successes">
  <span><b>Successful</b> 10,000 yuan annual</span><span><b>Successful</b> 10,000 yuan annual</span>
  <span><b>Successful</b> 10,000 yuan annual</span><span><b>Successful</b> 10,000 yuan annual</span>
</div>

<section class="stats">
  <div class="wrap">
    <div class="stat"><div class="v">¥ 233235</div><div class="k">Funding total</div></div>
    <div class="stat"><div class="v">14.69%</div><div class="k">Average yield</div></div>
    <div class="stat wide"><div class="v">12.23 Month</div><div class="k">The average duration of</div></div>
    <div class="cta"><svg class="ico" viewBox="0 0 40 40"><rect x="4" y="24" width="6" height="12" fill="#fff"/><rect x="14" y="16" width="6" height="20" fill="#fff"/><rect x="24" y="8" width="6" height="28" fill="#fff"/></svg><a>START INVESTING</a></div>
  </div>
</section>

<table class="loans">
  <thead><tr><th>The title loan</th><th>Credit rating</th><th>APR</th><th>Amount</th><th>Term</th><th>Progress</th><th></th></tr></thead>
  <tbody>
    <tr><td>Cash flow</td><td><span class="rate on">A</span> <span class="rate">B</span></td><td>15.0%</td><td>10,000 yuan</td><td>12 months</td><td>5.23%</td><td class="go">Start lending</td></tr>
    <tr><td>Short-term liquidity</td><td><span class="rate on">A</span></td><td>13.0%</td><td>30,000 yuan</td><td>12 months</td><td>15.00%</td><td class="go">Start lending</td></tr>
    <tr><td>Short-term liquidity</td><td><span class="rate on">B</span></td><td>13.0%</td><td>8750.0 yuan</td><td>6 months</td><td>30.00%</td><td class="go">Start lending</td></tr>
    <tr><td>Business Loans</td><td><span class="rate on">A</span></td><td>14.0%</td><td>20,000 yuan</td><td>24 months</td><td>81.23%</td><td class="go">Start lending</td></tr>
    <tr><td>Expand Business</td><td><span class="rate on">A</span></td><td>15.0%</td><td>50,000 yuan</td><td>12 months</td><td>100.0%</td><td class="full">Full scale</td></tr>
    <tr><td>Short-term liquidity</td><td><span class="rate on">B</span></td><td>12.0%</td><td>10,000 yuan</td><td>6 months</td><td>100.0%</td><td class="full">Full scale</td></tr>
  </tbody>
</table>

<h2 class="section-title" style="top:1492px">Fixed Products</h2>
<section class="products">
  <div class="product photo" role="img" aria-label="Promotional photo with the word NOW">NOW</div>
  <div class="product o"><div class="t">6 month rate of return</div><div class="pct">11.0%</div><div class="s">The remaining 26 years, reach 10,000 yuan</div></div>
  <div class="product b"><div class="t">9 month rate of return</div><div class="pct">12.0%</div><div class="s">The remaining 26 years, reach 10,000 yuan</div></div>
  <div class="product r"><div class="t">12 month rate of return</div><div class="pct">13.0%</div><div class="s">The remaining 26 years, reach 10,000 yuan</div></div>
</section>

<section class="social">
  <div class="wrap">
    <div class="panel">
      <h4>Testimonials</h4>
      <div class="testi"><div class="avatar" role="img" aria-label="Customer portrait"></div>
        <p>I started lending last spring and the monthly interest has been steady. Simple, clear and safe. <span class="who">Lin Wei, lender</span></p></div>
    </div>
    <div class="panel">
      <h4>Join The Newsletter</h4>
      <div class="note">Sign up to receive new loans and offers first</div>
      <div class="signup"><span>Your email address</span><b>Sign up</b></div>
    </div>
  </div>
</section>

<h2 class="section-title" style="top:1968px">Our Partner</h2>
<section class="partners">
  <div class="partner"><i></i>Norvale Direct</div>
  <div class="partner"><i></i>Eastbridge Microcredit Union</div>
  <div class="partner t"><i></i>Quanlet Cloud</div>
</section>

<footer class="footer">
  <div class="wrap">
    <div class="fcol links">
      <div><h5>Kelvo.cn</h5><ul><li>Investment</li><li>Credit</li><li>Media</li><li>Cooperation</li></ul></div>
      <div><h5>&nbsp;</h5><ul><li>About Us</li><li>Contact Us</li><li>Join us</li><li>Privacy Policy</li></ul></div>
    </div>
    <div class="fcol service"><h5>Customer Service</h5><ul><li>400-555-0188</li></ul><div class="icons"><i></i><i></i><i></i><i></i></div><ul><li>service@kelvo.cn</li></ul></div>
    <div class="fcol address"><h5>Our Address</h5><ul><li>Room 1208, Lantern Tower, 88 Harbor Road</li><li>Xuhui District, Shanghai</li><li>400-555-0188</li><li>info@kelvo.cn</li></ul></div>
  </div>
  <div class="copy">© 2014 Kelvo.cn All rights reserved</div>
</footer>

</body>
</html>
```